Fantasy Sports Website Needs Web Design

We are modeling our site functionality from www.brisklinepicks.com using the same backend systems, and our site will be Rostervault.com with the logo branding attached.
The site should have the following pages: home page, signup pages, games/lobby, rules, live scoring, support/FAQs, contact us.
There should be navication in the footer of the page that includes the different pages along with the Privacy Policy and Terms of Use.

Target Market(s)
•	80% Male
•	89.8% Caucasian
•	51.5% Not Married
•	Average Age: 34
•	College Degree or More: 78.1%
•	51.6% play video games
•	19% play online poker
•	Stats fairly in line with young male demographic
Number of Pages Required
2 page
Look and feel
Each slider illustrates characteristics of the customer's brand and the style your logo design should communicate.

```html
<!DOCTYPE html>
<html lang="en">
<head>
<meta charset="utf-8">
<title>Rostervault – Fantasy Sports</title>
<link href="https://fonts.googleapis.com/css2?family=Oswald:wght@500;700&family=Open+Sans:wght@300;400;600;700&display=swap" rel="stylesheet">
<style>
:root{
  --navy-dark:#06121f;
  --navy:#17375a;
  --orange:#e8830f;
  --red:#b3171c;
  --deep-red:#8e0a14;
  --body-bg:#1e1e1e;
  --footer-bg:#000;
  --bar-bg:#0e0e0e;
  --nav-top:#ececec;
  --nav-bottom:#b4b4b4;
  --ink:#1d1d1d;
  --muted:#9a9a9a;
  --link:#8a8a8a;
  --white:#fff;
}
*{margin:0;padding:0;box-sizing:border-box}
html,body{width:1014px;height:1200px;overflow:hidden;background:var(--body-bg)}
body{position:relative;font-family:'Open Sans',sans-serif;color:var(--white)}
.abs{position:absolute}
.condensed{font-family:'Oswald',sans-serif;text-transform:uppercase}

/* header */
.topbar{left:0;top:0;width:1014px;height:97px;
  background:
    radial-gradient(ellipse 45% 90% at 50% 30%,rgba(40,80,120,.55),transparent 70%),
    radial-gradient(ellipse 30% 80% at 15% 60%,rgba(30,60,95,.5),transparent 70%),
    linear-gradient(180deg,var(--navy) 0%,var(--navy-dark) 100%)}
.phone-icon{left:146px;top:27px;width:43px;height:43px}
.call-label{left:201px;top:27px;font-size:14px;font-weight:700;letter-spacing:.2px}
.call-number{left:201px;top:44px;font-size:18px;font-weight:700;color:var(--orange);letter-spacing:.3px}
.register{left:634px;top:46px;font-size:14px;font-weight:700}
.login-btn{left:763px;top:36px;width:106px;height:34px;border:2px solid var(--orange);color:var(--orange);font-size:14px;font-weight:700;display:flex;align-items:center;justify-content:center}

/* nav */
.nav{left:0;top:97px;width:1014px;height:38px;background:linear-gradient(var(--nav-top),var(--nav-bottom));box-shadow:0 2px 4px rgba(0,0,0,.4)}
.nav-item{top:97px;height:38px;display:flex;align-items:center;font-size:11.5px;font-weight:700;color:var(--ink);padding:0 21px;border-left:1px solid #a8a8a8}
.brand{left:407px;top:96px;width:220px;height:40px;display:flex;align-items:center;justify-content:center;gap:8px;font-family:'Oswald',sans-serif;font-weight:700;font-size:26px;letter-spacing:1px;color:var(--ink);text-transform:uppercase}
.brand-dot{width:12px;height:12px;border-radius:50%;background:var(--red)}

/* hero */
.hero{left:0;top:135px;width:1014px;height:355px;
  background:
    linear-gradient(180deg,transparent 70%,rgba(20,10,10,.55) 100%),
    radial-gradient(ellipse 28% 45% at 42% 62%,rgba(255,200,110,.85),transparent 70%),
    radial-gradient(ellipse 40% 60% at 10% 55%,rgba(120,45,20,.9),transparent 75%),
    radial-gradient(ellipse 35% 45% at 92% 20%,rgba(205,160,170,.8),transparent 70%),
    radial-gradient(ellipse 45% 35% at 75% 85%,rgba(150,95,55,.8),transparent 75%),
    linear-gradient(100deg,#3a1c18 0%,#8e3c1c 25%,#c2682a 42%,#6a3c3a 62%,#5b3f55 82%,#9d7380 100%)}
.hero-one{left:548px;top:224px;font-size:60px;font-weight:700;color:var(--deep-red);line-height:1}
.hero-leagues{left:548px;top:292px;font-size:30px;font-weight:700;line-height:1}
.hero-lobby{left:548px;top:334px;font-size:39px;font-weight:700;color:var(--orange);line-height:1}
.arrow-btn{top:452px;width:24px;height:24px;background:var(--red);display:flex;align-items:center;justify-content:center}

/* tiles */
.tile{top:510px;width:229px;height:173px;overflow:hidden;box-shadow:0 2px 6px rgba(0,0,0,.5)}
.tile::after{content:"";position:absolute;inset:0;background:linear-gradient(180deg,transparent 40%,rgba(10,10,10,.75) 100%)}
.tile-title{position:absolute;z-index:1;left:16px;top:108px;font-size:18px;font-weight:700;color:var(--orange);text-transform:uppercase;white-space:nowrap}
.tile-sub{position:absolute;z-index:1;left:16px;top:133px;font-size:20px;font-weight:300;text-transform:uppercase;white-space:nowrap}

/* news */
.section-title{left:164px;top:706px;font-size:15px;font-weight:700}
.news-card{top:744px;width:158px}
.news-photo{width:158px;height:102px;position:relative}
.news-date{position:absolute;left:4px;bottom:6px;width:100px;height:22px;background:rgba(0,0,0,.75);color:var(--orange);font-size:9.5px;font-weight:700;display:flex;align-items:center;justify-content:center}
.news-title{margin-top:13px;font-size:10px;font-weight:700;color:var(--red);padding-left:1px}
.news-text{margin-top:5px;font-size:9.5px;line-height:18px;color:var(--muted);padding-left:1px}

/* footer */
.footer{left:0;top:945px;width:1014px;height:213px;background:var(--footer-bg)}
.footer-brand{left:170px;top:1040px;display:flex;align-items:center;gap:8px;font-family:'Oswald',sans-serif;font-weight:700;font-size:26px;letter-spacing:1px;color:var(--white);text-transform:uppercase}
.footer-col{top:978px}
.footer-col h3{font-size:11px;font-weight:700;color:var(--orange);margin-bottom:10px}
.footer-col li{list-style:none;font-size:8px;color:var(--link);line-height:19px;text-transform:uppercase}
.social{list-style:none}
.social li{display:flex;align-items:center;gap:6px;height:20px;margin-bottom:9px;font-size:8px;color:var(--link);text-transform:uppercase}
.social-box{width:20px;height:20px;border:1px solid #4a4a4a;background:linear-gradient(#222,#141414);display:flex;align-items:center;justify-content:center}
.social-box::before{content:"";width:6px;height:6px;border-radius:50%;background:#9a9a9a}
.bottom-bar{left:0;top:1158px;width:1014px;height:42px;background:var(--bar-bg);display:flex;align-items:center;justify-content:center;font-size:7.5px;color:#6d6d6d}
</style>
</head>
<body>

<header>
  <div class="abs topbar"></div>
  <svg class="abs phone-icon" viewBox="0 0 43 43" aria-hidden="true">
    <circle cx="21.5" cy="21.5" r="20" fill="none" stroke="#e8830f" stroke-width="2"/>
    <path d="M14 13c2-2 4-1 5 1l1 3c0 1-1 2-2 3 1 3 3 5 6 6 1-1 2-2 3-2l3 1c2 1 3 3 1 5-3 3-8 1-12-3s-7-10-5-14z" fill="#e8830f"/>
  </svg>
  <div class="abs call-label condensed">Call us :</div>
  <div class="abs call-number condensed">(3180) 552 714</div>
  <div class="abs register condensed">New users register</div>
  <div class="abs login-btn condensed">Users login</div>
</header>

<nav>
  <div class="abs nav"></div>
  <div class="abs nav-item" style="left:146px">HOME</div>
  <div class="abs nav-item" style="left:214px">ABOUT US</div>
  <div class="abs nav-item" style="left:305px">SERVICES</div>
  <div class="abs brand"><span class="brand-dot"></span>Rostervault</div>
  <div class="abs nav-item" style="left:631px">VIDEO</div>
  <div class="abs nav-item" style="left:702px">SPONCERS</div>
  <div class="abs nav-item" style="left:795px;border-right:1px solid #a8a8a8">CONTACT US</div>
</nav>

<section>
  <div class="abs hero" role="img" aria-label="Mountain biker riding over rocky peaks at sunset"></div>
  <div class="abs hero-one condensed">One day</div>
  <div class="abs hero-leagues condensed">Fantasy sports leagues</div>
  <div class="abs hero-lobby condensed">Enter game lobby</div>
  <div class="abs arrow-btn" style="left:803px"><svg width="10" height="12" viewBox="0 0 10 12"><path d="M7 1 2 6l5 5" stroke="#fff" stroke-width="1.6" fill="none"/></svg></div>
  <div class="abs arrow-btn" style="left:828px"><svg width="10" height="12" viewBox="0 0 10 12"><path d="M3 1l5 5-5 5" stroke="#fff" stroke-width="1.6" fill="none"/></svg></div>
</section>

<section>
  <div class="abs tile" style="left:153px;background:radial-gradient(ellipse 60% 55% at 65% 30%,#e2622a,transparent 75%),radial-gradient(ellipse 50% 40% at 20% 15%,#f08a3a,transparent 70%),linear-gradient(160deg,#b8401a,#6e1d0c 60%,#1e0b06)" role="img" aria-label="Footballer kicking a ball against a fiery sky">
    <div class="tile-title">Rostervault</div><div class="tile-sub">Sports visit</div>
  </div>
  <div class="abs tile" style="left:393px;background:radial-gradient(ellipse 25% 40% at 78% 40%,rgba(230,170,90,.55),transparent 75%),radial-gradient(ellipse 20% 25% at 50% 48%,rgba(200,70,60,.5),transparent 75%),linear-gradient(180deg,#1d2767 0%,#17195a 45%,#0d1025 62%,#121212 100%)" role="img" aria-label="City skyline with hotel towers at night">
    <div class="tile-title">Rostervault</div><div class="tile-sub">Atlantic city</div>
  </div>
  <div class="abs tile" style="left:633px;background:radial-gradient(ellipse 35% 45% at 50% 35%,#8a6a5a,transparent 75%),radial-gradient(ellipse 60% 30% at 50% 5%,#a8b0ba,transparent 75%),linear-gradient(180deg,#6b7480,#3d434b 55%,#1a1c1f)" role="img" aria-label="Swimmer in cap and goggles mid stroke">
    <div class="tile-title">Rostervault</div><div class="tile-sub">Latest sports</div>
  </div>
</section>

<section>
  <h2 class="abs section-title">LATEST NEWS</h2>
  <article class="abs news-card" style="left:164px">
    <div class="news-photo" style="background:radial-gradient(ellipse 35% 50% at 45% 45%,#8a6a55,transparent 75%),linear-gradient(135deg,#4e5260,#1e1f24)" role="img" aria-label="Bodybuilder flexing"><div class="news-date">27 MARCH 2015</div></div>
    <div class="news-title">LOREM IPSUM IS A DUMMY</div>
    <p class="news-text">Lorem Ipsum is simply dummy<br>text of the printing...</p>
  </article>
  <article class="abs news-card" style="left:341px">
    <div class="news-photo" style="background:radial-gradient(ellipse 40% 40% at 55% 40%,#c48a50,transparent 75%),linear-gradient(180deg,#f3efe6,#e0c8a4 50%,#5d9aa4 88%,#3d6f78)" role="img" aria-label="Skateboarder crouching by the sea"><div class="news-date">27 MARCH 2015</div></div>
    <div class="news-title">LOREM IPSUM IS A DUMMY</div>
    <p class="news-text">Lorem Ipsum is simply dummy<br>text of the printing...</p>
  </article>
  <article class="abs news-card" style="left:518px">
    <div class="news-photo" style="background:radial-gradient(ellipse 35% 45% at 60% 30%,#c9a48e,transparent 75%),linear-gradient(135deg,#222,#9a9a9a 35%,#e8e8e8 60%,#fff)" role="img" aria-label="Ice hockey player in helmet"><div class="news-date">27 MARCH 2015</div></div>
    <div class="news-title">LOREM IPSUM IS A DUMMY</div>
    <p class="news-text">Lorem Ipsum is simply dummy<br>text of the printing...</p>
  </article>
  <article class="abs news-card" style="left:695px">
    <div class="news-photo" style="background:radial-gradient(ellipse 40% 45% at 55% 50%,#c89a6a,transparent 75%),linear-gradient(135deg,#5a3a22,#8d6540 50%,#2e1e10)" role="img" aria-label="Boxer throwing a punch"><div class="news-date">27 MARCH 2015</div></div>
    <div class="news-title">LOREM IPSUM IS A DUMMY</div>
    <p class="news-text">Lorem Ipsum is simply dummy<br>text of the printing...</p>
  </article>
</section>

<footer>
  <div class="abs footer"></div>
  <div class="abs footer-brand"><span class="brand-dot"></span>Rostervault</div>
  <div class="abs footer-col" style="left:379px">
    <h3>WELCOME</h3>
    <ul><li>Home</li><li>About us</li><li>Services</li><li>Video</li><li>Sponcers</li><li>Contact us</li></ul>
  </div>
  <div class="abs footer-col" style="left:495px">
    <h3>SERVICES</h3>
    <ul><li>Events</li><li>Fighters</li><li>Videos</li><li>Photos</li><li>Pay-per-view</li><li>News</li><li>Tickets</li></ul>
  </div>
  <div class="abs footer-col" style="left:603px">
    <h3>INFORMATION</h3>
    <ul><li>Privacy policy</li><li>Terms &amp; conditions</li><li>Sitemap</li></ul>
  </div>
  <div class="abs footer-col" style="left:745px">
    <h3>FOLLOW US</h3>
    <ul class="social">
      <li><span class="social-box"></span>: Friendwall</li>
      <li><span class="social-box"></span>Chirper</li>
      <li><span class="social-box"></span>: Circlenet</li>
      <li><span class="social-box"></span>: Worklink</li>
    </ul>
  </div>
  <div class="abs bottom-bar">COPYRIGHTS © 2015. ROSTERVAULT. ALL RIGHTS RESERVED.</div>
</footer>

</body>
</html>
```